KVR Trifold for Tradeshows/Cold Calls

We need an update to our current tri-fold layout. The content can stay the same, but we are looking for some more innovative design. We don't want the trifold larger than a standard piece of paper (8.5 x 11) when folded but we are open to different sizes. This is a rush project - we have a tradeshow coming up and need these finalized and printed right away! Please reach out at any time with questions or need more pictures!

Font styles to use
Other font styles liked:
• Tahoma

Colors
0555a3
33a6d7

Requirements
Must have
• Pictures
• Unique Design
• Good flow
• Correct company colors
• Space for testimonials
Should not have
• blank space
• awkwardness
• colors outside of brand

```html
<!DOCTYPE html>
<html lang="en">
<head>
<meta charset="utf-8">
<title>KVR Trifold</title>
<link href="https://fonts.googleapis.com/css2?family=PT+Sans:wght@400;700&family=Roboto+Condensed:wght@400;700&display=swap" rel="stylesheet">
<style>
:root{
  --brand-blue:#0555a3;
  --brand-sky:#33a6d7;
  --panel-blue:#2a5ba8;
  --ink:#3c3c3c;
  --muted:#6a6a6a;
  --paper:#ffffff;
  --stage:#d9d9d9;
}
*{margin:0;padding:0;box-sizing:border-box}
html,body{width:1200px;height:1200px;overflow:hidden;background:var(--stage)}
body{position:relative;font-family:"Roboto Condensed",Arial,sans-serif;color:var(--ink)}
.spread{position:absolute;left:102px;width:997px;height:430px;background:var(--paper);overflow:hidden}
.spread--outside{top:106px}
.spread--inside{top:664px}
.abs{position:absolute}
.heading{font-family:"PT Sans",Tahoma,sans-serif;font-weight:700;color:var(--brand-blue);text-transform:uppercase;line-height:1.05}

/* wordmark */
.wordmark{display:flex;flex-direction:column;align-items:flex-start}
.wordmark__name{display:flex;align-items:center;gap:4px;font-family:"PT Sans",Tahoma,sans-serif;font-weight:700;line-height:1}
.wordmark__dot{display:inline-block;background:var(--brand-sky)}
.wordmark__tag{font-size:4.6px;letter-spacing:.2px;text-transform:uppercase;margin-top:2px}
.wordmark--light .wordmark__name,.wordmark--light .wordmark__tag{color:#fff}
.wordmark--brand .wordmark__name{color:var(--brand-blue)}
.wordmark--brand .wordmark__tag{color:var(--brand-blue)}

/* outside spread */
.cover-band{left:0;top:0}
.specialties{left:28px;top:72px}
.specialties__title{font-size:15px;text-decoration:underline;text-decoration-thickness:1px;text-underline-offset:2px}
.specialties__list{list-style:none;margin-top:6px}
.specialties__list li{font-size:7.6px;line-height:13.3px;color:var(--muted);padding-left:8px;position:relative}
.specialties__list li::before{content:"";position:absolute;left:0;top:4.8px;width:4px;height:4px;border-radius:50%;background:var(--brand-sky)}
.back-mark{left:243px;top:382px}
.back-mark .wordmark__name{font-size:18px}
.back-url{left:243px;top:407px;font-size:6.6px;color:#fff}
.contact{left:398px;width:200px;top:172px;text-align:center;color:#fff}
.contact .wordmark{align-items:center}
.contact .wordmark__name{font-size:25px}
.contact__lines{font-size:6.4px;line-height:8.6px;margin-top:14px}
.contact__phone{font-size:6.4px;margin-top:8px}
.contact__phone b{font-weight:700}
.contact__url{font-size:6.4px;margin-top:9px}
.cover-photo{left:664px;top:0}
.cover-mark{left:664px;width:333px;top:30px;display:flex;flex-direction:column;align-items:center}
.cover-mark .wordmark{align-items:center}
.cover-mark .wordmark__name{font-size:29px}
.cover-regions{font-size:5px;color:var(--ink);margin-top:8px}
.cover-title{right:120px;top:151px;text-align:right;font-size:13.4px;color:var(--brand-blue);font-family:"PT Sans",Tahoma,sans-serif;line-height:15px;text-transform:uppercase}
.cover-title b{font-weight:700}
.cover-title span{display:block}
.cover-title .indent-a{padding-right:0}
.cover-title .indent-b{padding-right:10px}
.cover-title .indent-c{padding-right:28px}
.cover-title .indent-d{padding-right:5px}
.cover-url{right:18px;top:412px;font-size:5.6px;color:var(--ink)}

/* inside spread */
.facade-photo{left:0;top:0}
.about{left:247px;top:169px;width:198px;height:210px;background:var(--brand-blue);color:#fff}
.about p{position:absolute;left:99px;top:28px;width:86px;font-size:6.8px;line-height:10px;text-align:justify;letter-spacing:.2px}
.inside-mark{left:362px;top:76px}
.inside-mark .wordmark__name{font-size:24px}
.safety{left:468px;top:48px;width:162px}
.safety .heading,.roi .heading{font-size:13.6px}
.safety p{font-size:6.1px;line-height:9px;color:var(--muted);margin-top:9px;text-align:justify}
.roi{left:468px;top:165px;width:162px}
.roi__list{list-style:none;margin-top:6px}
.roi__item{display:flex;gap:8px;margin-bottom:8px;align-items:flex-start}
.roi__item svg{flex:0 0 18px;margin-top:2px}
.roi__item h3{font-size:7.2px;font-weight:700;color:var(--ink)}
.roi__item p{font-size:6px;line-height:8.8px;color:var(--muted);text-align:justify}
.testimonials{left:665px;top:26px;width:157px;height:182px;background:var(--brand-blue);color:#fff;padding:14px 11px 0}
.quote p{font-size:4.9px;line-height:8px;text-align:justify}
.quote cite{display:block;font-style:normal;text-align:right;margin-top:6px}
.quote cite b{display:block;font-size:7px;font-weight:700;font-family:"PT Sans",Tahoma,sans-serif}
.quote cite span{font-size:5px}
.quote + .quote{margin-top:20px}
.job-photo{position:absolute;width:128px}
</style>
</head>
<body>

<!-- OUTSIDE SPREAD -->
<section class="spread spread--outside">
  <svg class="abs cover-band" width="664" height="430" role="img" aria-label="Blue-tinted photo of a glass office tower with a window-cleaning platform and treetops below">
    <defs>
      <linearGradient id="bandTint" x1="0" y1="0" x2="1" y2="1">
        <stop offset="0" stop-color="#4a78bd"/>
        <stop offset=".5" stop-color="#2f5fab"/>
        <stop offset="1" stop-color="#244f98"/>
      </linearGradient>
    </defs>
    <polygon points="213,0 664,0 664,430 120,430" fill="url(#bandTint)"/>
    <rect x="332" y="0" width="332" height="430" fill="#2a5aa7" opacity=".35"/>
  </svg>

  <div class="abs specialties">
    <h2 class="heading specialties__title">Specializing In</h2>
    <ul class="specialties__list">
      <li>Sealants &amp; Caulking</li>
      <li>Vertical Wall Coatings</li>
      <li>Below Grade Waterproofing</li>
      <li>Deck Coatings</li>
      <li>Expansion Joint Systems</li>
      <li>Parking Deck Waterproofing</li>
      <li>Clear Water Repellants</li>
      <li>Grout &amp; Epoxy Injections</li>
      <li>Heavy Traffic Coating</li>
      <li>Parking Deck Re-Striping</li>
      <li>Leak Service Calls</li>
      <li>Concrete Repair &amp; Replacement</li>
      <li>Masonry Repair &amp; Replacement</li>
      <li>Cleaning, Coating and Sealer</li>
      <li>Glazed Curtain Wall/Storefront</li>
      <li>Facade Reconstruction</li>
      <li>Tuck-Pointing</li>
      <li>Stucco &amp; EIFS Systems</li>
      <li>Window Gasket Replacement</li>
      <li>Pressure Washing</li>
    </ul>
  </div>

  <div class="abs back-mark wordmark wordmark--light">
    <span class="wordmark__name">KVR <i class="wordmark__dot" style="width:6px;height:6px"></i></span>
    <span class="wordmark__tag">Waterproofing · Restoration</span>
  </div>
  <div class="abs back-url">www.KVRwp.com</div>

  <div class="abs contact">
    <div class="wordmark wordmark--light">
      <span class="wordmark__name">KVR <i class="wordmark__dot" style="width:8px;height:8px"></i></span>
      <span class="wordmark__tag">Waterproofing · Restoration</span>
    </div>
    <div class="contact__lines">240 Harlow Lane, PO Box 316<br>Millbrook, NC 27999</div>
    <div class="contact__phone"><b>Phone:</b> 877 555 0142 &nbsp;&nbsp; <b>Fax:</b> 919 555 0187</div>
    <div class="contact__url">www.KVRwp.com</div>
  </div>

  <svg class="abs cover-photo" width="333" height="430" role="img" aria-label="Upward view of glass skyscrapers against a pale sky, fading to white at the top">
    <defs>
      <linearGradient id="coverFade" x1="0" y1="0" x2="0" y2="1">
        <stop offset="0" stop-color="#ffffff"/>
        <stop offset=".25" stop-color="#eef0f3"/>
        <stop offset=".6" stop-color="#c9ced6"/>
        <stop offset="1" stop-color="#9aa3b0"/>
      </linearGradient>
      <linearGradient id="coverBlue" x1="0" y1="0" x2="1" y2="1">
        <stop offset="0" stop-color="#1f4f8e" stop-opacity=".85"/>
        <stop offset="1" stop-color="#0555a3" stop-opacity=".6"/>
      </linearGradient>
    </defs>
    <rect width="333" height="430" fill="url(#coverFade)"/>
    <path d="M0 90 L60 120 L120 430 L0 430 Z" fill="url(#coverBlue)" opacity=".55"/>
    <path d="M230 80 L333 60 L333 380 L290 350 Z" fill="url(#coverBlue)" opacity=".5"/>
  </svg>

  <div class="abs cover-mark">
    <div class="wordmark wordmark--brand">
      <span class="wordmark__name">KVR <i class="wordmark__dot" style="width:9px;height:9px"></i></span>
      <span class="wordmark__tag">Waterproofing · Restoration</span>
    </div>
    <div class="cover-regions">North Carolina | South Carolina | Virginia</div>
  </div>

  <h1 class="abs cover-title">
    <span class="indent-a"><b>Protecting and</b></span>
    <span class="indent-b"><b>Enhancing</b></span>
    <span class="indent-c">Your Property</span>
    <span class="indent-d">Investment</span>
  </h1>
  <div class="abs cover-url">www.KVRwp.com</div>
</section>

<!-- INSIDE SPREAD -->
<section class="spread spread--inside">
  <svg class="abs facade-photo" width="332" height="430" role="img" aria-label="Glass curtain-wall building reflecting a blue sky and clouds, with a window-washing platform near the top">
    <defs>
      <linearGradient id="facadeSky" x1="0" y1="0" x2="1" y2="1">
        <stop offset="0" stop-color="#6fa6de"/>
        <stop offset=".5" stop-color="#3d78bf"/>
        <stop offset="1" stop-color="#22507f"/>
      </linearGradient>
    </defs>
    <rect width="332" height="430" fill="url(#facadeSky)"/>
  </svg>

  <div class="abs about">
    <p>KVR is a commercial waterproofing and restoration company providing quality service to our loyal clientele and partners in North Carolina, South Carolina and Virginia. For over 14 years, KVR has provided excellent customer care with every service we provide. Our experienced management team highly skilled technicians create a well established action plan to every project, ensuring consistency and quality.</p>
  </div>

  <div class="abs inside-mark wordmark wordmark--brand">
    <span class="wordmark__name">KVR <i class="wordmark__dot" style="width:7px;height:7px"></i></span>
    <span class="wordmark__tag">Waterproofing · Restoration</span>
  </div>

  <div class="abs safety">
    <h2 class="heading">Safety is our<br>#1 priority!</h2>
    <p>KVR is committed to providing our employees and our clients with a safe work environment. Our area of expertise takes us into workplaces that are literally above the norm, and we take many steps to ensure that we are in compliance with any and all regulations that are associated with the work we perform.</p>
  </div>

  <div class="abs roi">
    <h2 class="heading">Return on<br>Investment</h2>
    <ul class="roi__list">
      <li class="roi__item">
        <svg width="18" height="18" viewBox="0 0 18 18" fill="none" stroke="var(--brand-blue)" stroke-width="1.6"><path d="M15 9a6 6 0 0 1-10.5 4M3 9a6 6 0 0 1 10.5-4"/><path d="M13.5 2v3h-3M4.5 16v-3h3"/></svg>
        <div><h3>Restore</h3><p>Return your building to pristine conditions.</p></div>
      </li>
      <li class="roi__item">
        <svg width="18" height="18" viewBox="0 0 18 18" fill="none" stroke="var(--brand-blue)" stroke-width="1.4"><path d="M2 2l5 5M7 4v3H4M16 2l-5 5M11 4v3h3M2 16l5-5M4 11h3v3M16 16l-5-5M14 11h-3v3"/></svg>
        <div><h3>Reduce</h3><p>Reduce negative air flow by sealing voids; energy savings.</p></div>
      </li>
      <li class="roi__item">
        <svg width="18" height="18" viewBox="0 0 18 18" fill="none" stroke="var(--brand-blue)" stroke-width="1.8"><circle cx="9" cy="9" r="7"/><path d="M4 14L14 4"/></svg>
        <div><h3>Avoid</h3><p>Avoid tenant disruption and frustration due to water and air infiltrations.</p></div>
      </li>
      <li class="roi__item">
        <svg width="18" height="18" viewBox="0 0 18 18" fill="none" stroke="var(--brand-blue)" stroke-width="1.3"><rect x="7" y="3" width="10" height="8"/><circle cx="4" cy="5" r="1.6" fill="var(--brand-blue)"/><path d="M4 7v6M2 9h5M3 16l1-3 1 3M9 9l3-3 2 2M12 11v5"/></svg>
        <div><h3>Demonstration</h3><p>Show tenants, employees and investors that you practice diligent building care and maintenance.</p></div>
      </li>
      <li class="roi__item">
        <svg width="18" height="18" viewBox="0 0 18 18" fill="none" stroke="var(--brand-blue)" stroke-width="1.2"><circle cx="8" cy="8" r="6.5"/><path d="M10 5.5H7a1.3 1.3 0 0 0 0 2.6h2a1.3 1.3 0 0 1 0 2.6H6M8 4v1.5M8 10.7v1.5"/><circle cx="13.5" cy="13.5" r="3" fill="#fff"/><path d="M13.5 12v1.6l1 .8"/></svg>
        <div><h3>Limit</h3><p>Limit unexpected costs, like those arising from a due diligence report.</p></div>
      </li>
    </ul>
  </div>

  <div class="abs testimonials">
    <blockquote class="quote">
      <p>KVR was a fantastic resource for Crestline Partners as they worked with me on behalf of my client to reposition a building that had substantial deferred maintenance. The client was in town for the third time since the work was completed and continue to marvel about the improvement to their asset. I would highly recommend KVR based on their professionalism, pricing and performance.</p>
      <cite><b>DANA WHITLOCK, RPA</b><span>Director, Property Manager Crestline Partners</span></cite>
    </blockquote>
    <blockquote class="quote">
      <p>KVR did an outstanding job of performing the work and equally important, coordinating with the building occupants. There were no complaints throughout the project which was amazing in itself. The project was completed on time and on budget. I highly recommend working with KVR and hope to have the opportunity to work with them in the future.</p>
      <cite><b>PAUL R. HENSLEY</b><span>Resident Architect, Ridgeview Academy</span></cite>
    </blockquote>
  </div>

  <svg class="job-photo" style="left:840px;top:26px" height="85" role="img" aria-label="Green boom lift beside a glass storefront among trees"><rect width="128" height="85" fill="#6f8f6a"/><rect y="30" width="128" height="30" fill="#9fb3c0" opacity=".7"/></svg>
  <svg class="job-photo" style="left:840px;top:123px" height="86" role="img" aria-label="Technician in a hard hat and safety vest on a building ledge"><rect width="128" height="86" fill="#a88a5e"/><rect y="60" width="128" height="26" fill="#3b8f6d" opacity=".7"/></svg>
  <svg class="job-photo" style="left:694px;top:221px" height="85" role="img" aria-label="Boom lift raised against a brick building and blue sky"><rect width="128" height="85" fill="#6f9fd6"/><rect y="45" width="128" height="40" fill="#8a5a44" opacity=".75"/></svg>
  <svg class="job-photo" style="left:840px;top:221px" height="85" role="img" aria-label="Two workers in safety vests replacing window gaskets on a red-framed window"><rect width="128" height="85" fill="#7a3b2c"/><rect x="10" y="10" width="108" height="65" fill="#b6b09a" opacity=".45"/></svg>
  <svg class="job-photo" style="left:694px;top:320px" height="85" role="img" aria-label="Green lift working along a glass curtain wall"><rect width="128" height="85" fill="#7f9a6f"/><rect y="20" width="128" height="40" fill="#a7b8c4" opacity=".7"/></svg>
  <svg class="job-photo" style="left:840px;top:320px" height="85" role="img" aria-label="Worker in a green aerial lift beside a brick facade"><rect width="128" height="85" fill="#94583f"/><rect x="40" y="25" width="45" height="60" fill="#3e9a55" opacity=".7"/></svg>
</section>

</body>
</html>
```